Web design for sitter site

We will be launching a sitter site in the coming months that focuses on sitters for children. The name of this site will be KinWatch.com
We will need:
1. main page design
2. site logo designed
3. subpages as well for the look of people's profiles, and job listings, etc (see links below)
We only need the design, photos, font files, etc. We do not need this site coded (no html), a ps job is fine.
Some competing sites in the space include - tendhaven.com and mindly.com
http://www.example-guardia.com/images/profile1.jpg
http://brookvaleshelf.example/wp-content/uploads/2013/09/mindly-review.png
http://www.pinecrestuni.example/hr/photos/tend_haven2.jpg
Thanks for your interest!
Target Market(s)
Mothers of children, mainly women
Industry/Entity Type
Online
Look and feel

```html
<!DOCTYPE html>
<html lang="en">
<head>
<meta charset="utf-8">
<title>KinWatch – find baby sitter</title>
<link href="https://fonts.googleapis.com/css2?family=Signika:wght@400;600&family=Quicksand:wght@400;500;700&family=Open+Sans:ital,wght@0,400;0,600;1,700&display=swap" rel="stylesheet">
<style>
:root{
  --cyan:#1ab4d8;
  --cyan-light:#20c0e8;
  --lime:#8fce00;
  --lime-dark:#7bb300;
  --lime-edge:#a6d92a;
  --grey-box:#9a9a9a;
  --grey-text:#7a7a7a;
  --ink:#444;
  --meta:#6aa3b8;
  --page:#ffffff;
  --section:#eeeee9;
  --panel:#f7f7f5;
  --footer:#464646;
  --footer-box:#5e5e5e;
  --footer-text:#d8d8d8;
  --red:#e8524a;
  --blue:#3a6fcf;
  --yellow:#f2c400;
}
*{box-sizing:border-box;margin:0;padding:0}
html,body{width:1125px;height:1200px;overflow:hidden;background:var(--page)}
body{position:relative;font-family:"Open Sans",sans-serif;color:var(--ink)}
.abs{position:absolute}

/* header */
.brand{left:187px;top:14px;display:flex;align-items:flex-start;gap:8px}
.brand-mark{width:34px;height:34px;border-radius:50%;background:var(--cyan);margin-top:6px}
.brand-name{font-family:"Signika",sans-serif;font-weight:600;font-size:30px;line-height:34px;color:var(--cyan)}
.brand-tag{font-family:"Signika",sans-serif;font-size:13px;color:var(--grey-text);margin-left:22px;line-height:14px}
.login{left:702px;top:22px;width:82px;height:27px;background:var(--lime);color:#fff;font-family:"Signika",sans-serif;font-weight:600;font-size:13px;letter-spacing:.5px;display:flex;align-items:center;justify-content:center}
.phone{left:798px;top:24px;display:flex;align-items:center;gap:4px;font-family:"Quicksand",sans-serif;font-weight:500;font-size:15px;color:var(--cyan);letter-spacing:.5px}

/* nav */
.nav{z-index:5;left:242px;top:78px;width:640px;height:32px;display:flex;font-family:"Signika",sans-serif;font-size:12.5px;color:#fff;box-shadow:0 6px 6px -4px rgba(0,0,0,.25)}
.nav-trust{width:338px;background:var(--cyan);display:flex;align-items:center;padding-left:13px;gap:20px;font-weight:600;white-space:nowrap}
.nav-parents{width:155px;background:var(--cyan-light);display:flex;align-items:center;justify-content:center;gap:6px;white-space:nowrap}
.nav-sitter{width:147px;background:var(--lime);display:flex;align-items:center;justify-content:center;gap:6px;white-space:nowrap}

/* hero */
.hero{left:0;top:92px;width:1125px;height:390px;background:linear-gradient(90deg,#f1f1f1,#f8f8f8 50%,#f1f1f1)}
.hero-photo{left:572px;top:130px;width:313px;height:352px;background:linear-gradient(160deg,#d9b08e 0%,#c38a66 40%,#7c4c9e 75%,#a9774f 100%);border-radius:140px 140px 0 0}
.hero-lead{left:264px;top:280px;font-family:"Quicksand",sans-serif;font-weight:700;font-size:29px;line-height:34px;color:#858585;letter-spacing:-.5px;white-space:nowrap}
.hero-title{left:229px;top:304px;font-family:"Quicksand",sans-serif;font-weight:500;font-size:41px;line-height:46px;color:var(--cyan);letter-spacing:-1px;white-space:nowrap}
.option{z-index:2;top:352px;height:117px;width:330px;padding:12px 18px;color:#fff;font-family:"Quicksand",sans-serif}
.option-care{left:226px;background:rgba(150,150,150,.95)}
.option-job{left:556px;background:var(--lime)}
.option h2{font-weight:400;font-size:21px;line-height:26px;white-space:nowrap}
.option h2 b{font-family:"Signika",sans-serif;font-weight:600}
.option p{font-size:17px;line-height:15px;margin-top:4px;width:280px}
.option .btn{position:absolute;left:22px;bottom:12px;width:102px;height:24px;display:flex;align-items:center;justify-content:center;font-family:"Signika",sans-serif;font-weight:600;font-size:12px;letter-spacing:.5px}
.option-care .btn{background:var(--lime)}
.option-job .btn{background:var(--grey-box)}

.stripe{z-index:3;left:0;width:1125px;height:2px;background:linear-gradient(90deg,var(--cyan) 0 14%,var(--red) 14% 28%,var(--blue) 28% 42%,var(--cyan) 42% 56%,var(--yellow) 56% 70%,var(--lime) 70% 84%,var(--cyan) 84%)}

/* sitters */
.section{left:0;top:484px;width:1125px;height:484px;background:var(--section)}
.tab{top:532px;height:29px;display:flex;align-items:center;justify-content:center;font-family:"Signika",sans-serif;font-size:12.5px}
.tab-new{left:188px;width:135px;background:var(--panel);border:1px solid #ddd;border-bottom:none;color:#555}
.tab-featured{left:326px;width:143px;background:var(--lime);color:#fff}
.panel{left:188px;top:561px;width:749px;height:349px;background:var(--panel)}
.card{top:582px;width:164px;font-size:8.5px;color:#9a9a9a}
.divider{top:582px;width:1px;height:302px;background:#e2e2e2}
.card-photo{width:164px;height:132px;border:2px solid #e5e5e5}
.card-name{margin-top:14px;font-family:"Signika",sans-serif;font-size:11px;color:#555;display:flex;gap:6px;align-items:center}
.card-meta{margin-top:6px;display:flex;gap:8px;align-items:center;font-size:8px}
.card-bio{margin-top:10px;font-size:8.8px;line-height:12px}
.view{width:106px;height:30px;background:var(--lime-dark);border:2px solid var(--lime-edge);color:#fff;font-style:italic;font-weight:700;font-size:9.5px;display:flex;align-items:center;justify-content:center}

/* footer */
.footer{left:0;top:968px;width:1125px;height:232px;background:var(--footer)}
.fbox{background:var(--footer-box);color:var(--footer-text)}
.fbox h3{font-family:"Signika",sans-serif;font-weight:600;font-size:14.5px;color:#fff}
.about{left:188px;top:1000px;width:238px;height:157px;padding:12px 17px}
.about p{margin-top:9px;font-size:9.6px;line-height:13px}
.about a{display:block;margin-top:11px;color:var(--lime);font-weight:600;font-size:10px;text-decoration:none}
.contact{left:439px;top:1000px;width:240px;height:67px;padding:14px 12px;font-family:"Signika",sans-serif;font-size:12px}
.contact div{display:flex;align-items:center;gap:9px;height:18px;margin-bottom:9px}
.dot{width:17px;height:17px;border-radius:50%;background:#1e1e1e;display:inline-block}
.news{left:693px;top:1000px;width:244px;height:67px;padding:10px 12px 10px 17px}
.news ul{list-style:none;display:flex;flex-wrap:wrap;gap:5px 14px;margin-top:6px;font-size:8px;color:#fff;white-space:nowrap}
.news li::before{content:"";display:inline-block;width:6px;height:6px;border-radius:50%;background:var(--lime);margin-right:6px}
.social{left:439px;top:1082px;width:498px;height:75px;padding:11px 18px}
.social h3{font-weight:400;font-size:13px}
.icons{display:flex;gap:11px;margin-top:15px}
.icons span{width:18px;height:18px;border-radius:50%;background:#111}
.subscribe{left:666px;top:1093px;font-family:"Signika",sans-serif;font-weight:400;font-size:13px;color:#fff}
.field{left:666px;top:1117px;width:187px;height:28px;background:#efefef;border-radius:7px;font-size:8.5px;color:#aaa;padding:8px 13px}
.send{left:858px;top:1116px;width:67px;height:30px;background:var(--lime);border-radius:7px;border:1px solid #b1e13a;color:#fff;font-family:"Signika",sans-serif;font-size:13px;display:flex;align-items:center;justify-content:center}
.legal{top:1171px;font-size:8.5px;color:#fff;white-space:nowrap}
</style>
</head>
<body>

<header>
  <div class="abs brand">
    <span class="brand-mark"></span>
    <div>
      <div class="brand-name">KinWatch</div>
      <div class="brand-tag">find baby sitter!</div>
    </div>
  </div>
  <div class="abs login">LOGIN</div>
  <div class="abs phone">
    <svg width="20" height="18" viewBox="0 0 20 18"><path d="M4 2c1-1 2-1 3 0l1.5 2.5c.5 1 0 1.6-.7 2.2 1 2 2.5 3.5 4.5 4.5.6-.7 1.2-1.2 2.2-.7L17 12c1 1 .8 2-.2 3l-1 1c-4 1-12-7-11-11z" fill="none" stroke="#1ab4d8" stroke-width="1.6"/></svg>
    1-800-555-0142
  </div>
</header>

<section>
  <div class="abs hero" role="img" aria-label="Soft grey background with a faint flower pattern"></div>
  <div class="abs hero-photo" role="img" aria-label="Photo of a smiling young girl with a teenage babysitter"></div>
  <div class="abs hero-lead">Let’s Get Started!</div>
  <div class="abs hero-title">choose an option!</div>
  <div class="abs option option-care">
    <h2>I need a <b>CAREGIVER!</b></h2>
    <p>Start your free search for care in your area.</p>
    <span class="btn">FIND CARE</span>
  </div>
  <div class="abs option option-job">
    <h2>I need a <b>CARE JOB!</b></h2>
    <p>Create a free profile and search for jobs.</p>
    <span class="btn">FIND JOB</span>
  </div>
  <div class="abs stripe" style="top:481px"></div>
</section>

<nav class="abs nav">
  <div class="nav-trust">TRUST &amp; SAFETY CENTER
    <svg width="160" height="10" viewBox="0 0 160 10"><path d="M2 6 C40 0 80 10 154 4" stroke="#bfeefb" stroke-dasharray="6 4" fill="none"/><path d="M150 1l5 3-5 3" stroke="#bfeefb" fill="none"/></svg>
  </div>
  <div class="nav-parents">
    <svg width="12" height="13" viewBox="0 0 12 13"><circle cx="6" cy="3.5" r="3" fill="#fff"/><path d="M1 13c0-4 2-6 5-6s5 2 5 6z" fill="#fff"/></svg>
    Signup For Parents
  </div>
  <div class="nav-sitter">
    <svg width="16" height="13" viewBox="0 0 16 13"><circle cx="5" cy="3.5" r="3" fill="#fff"/><circle cx="11" cy="4.5" r="2.5" fill="#fff"/><path d="M0 13c0-4 2-6 5-6s5 2 5 6zM9 13c0-3 1-5 3-5s4 2 4 5z" fill="#fff"/></svg>
    Signup For Sitter
  </div>
</nav>

<section>
  <div class="abs section" role="img" aria-label="Pale background with faint toy doodles"></div>
  <div class="abs tab tab-new">New Babysitters</div>
  <div class="abs tab tab-featured">Featured Babysitters</div>
  <div class="abs panel"></div>
  <div class="abs divider" style="left:374px"></div>
  <div class="abs divider" style="left:562px"></div>
  <div class="abs divider" style="left:748px"></div>

  <article class="abs card" style="left:201px">
    <div class="card-photo" role="img" aria-label="Portrait photo of a babysitter" style="background:linear-gradient(160deg,#d8d4cc,#9b7d6a 55%,#4a3528)"></div>
    <div class="card-name"><svg width="9" height="10"><circle cx="4.5" cy="2.5" r="2.3" fill="#6aa3b8"/><path d="M0 10c0-3 2-5 4.5-5s4.5 2 4.5 5z" fill="#6aa3b8"/></svg>Maren G.</div>
    <div class="card-meta"><svg width="8" height="10"><path d="M4 10C1 6 0 4.5 0 3.5a4 4 0 018 0C8 4.5 7 6 4 10z" fill="#6aa3b8"/><circle cx="4" cy="3.6" r="1.4" fill="#f7f7f5"/></svg>San Diego, CA</div>
    <div class="card-meta"><b style="color:var(--meta)">$</b>10-15</div>
    <p class="card-bio">Lorem Ipsum is simply dummy text of the printing and typesetting indu stry. Lorem Ipsum has been the industry's standard dummy text ever since</p>
    <div class="view" style="margin:14px 0 0 17px">View Profile</div>
  </article>

  <article class="abs card" style="left:388px">
    <div class="card-photo" role="img" aria-label="Photo of a sitter and a girl playing with sunglasses" style="background:linear-gradient(135deg,#6e7a5a,#2e2a2c 45%,#d14c86)"></div>
    <div class="card-name" style="margin-top:10px"><svg width="9" height="10"><circle cx="4.5" cy="2.5" r="2.3" fill="#6aa3b8"/><path d="M0 10c0-3 2-5 4.5-5s4.5 2 4.5 5z" fill="#6aa3b8"/></svg>Talia N.</div>
    <div class="card-meta"><svg width="8" height="10"><path d="M4 10C1 6 0 4.5 0 3.5a4 4 0 018 0C8 4.5 7 6 4 10z" fill="#6aa3b8"/><circle cx="4" cy="3.6" r="1.4" fill="#f7f7f5"/></svg>Gloucester, MA</div>
    <div class="card-meta"><b style="color:var(--meta)">$</b>10-20</div>
    <p class="card-bio">Lorem Ipsum is simply dummy text of the printing and typesetting indu stry. Lorem Ipsum has been the industry's standard dummy text ever since</p>
    <div class="view" style="margin:22px 0 0 29px">View Profile</div>
  </article>

  <article class="abs card" style="left:575px">
    <div class="card-photo" role="img" aria-label="Photo of a sitter and a child looking at a phone" style="background:linear-gradient(135deg,#8a4a2a,#c98a6a 45%,#5bbfa8 70%,#e07aa0)"></div>
    <div class="card-name" style="margin-top:11px"><svg width="9" height="10"><circle cx="4.5" cy="2.5" r="2.3" fill="#6aa3b8"/><path d="M0 10c0-3 2-5 4.5-5s4.5 2 4.5 5z" fill="#6aa3b8"/></svg>Talia N.</div>
    <div class="card-meta"><svg width="8" height="10"><path d="M4 10C1 6 0 4.5 0 3.5a4 4 0 018 0C8 4.5 7 6 4 10z" fill="#6aa3b8"/><circle cx="4" cy="3.6" r="1.4" fill="#f7f7f5"/></svg>Diamond Bar, CA</div>
    <div class="card-meta"><b style="color:var(--meta)">$</b>10-25</div>
    <p class="card-bio">Lorem Ipsum is simply dummy text of the printing and typesetting indus try. Lorem Ipsum has been the industry's standard dummy text ever since</p>
    <div class="view" style="margin:14px 0 0 29px">View Profile</div>
  </article>

  <article class="abs card" style="left:761px">
    <div class="card-photo" role="img" aria-label="Photo of a sitter baking with two boys in a kitchen" style="background:linear-gradient(135deg,#e9e6df,#b9a48c 50%,#3a4a6a)"></div>
    <div class="card-name" style="margin-top:11px"><svg width="9" height="10"><circle cx="4.5" cy="2.5" r="2.3" fill="#6aa3b8"/><path d="M0 10c0-3 2-5 4.5-5s4.5 2 4.5 5z" fill="#6aa3b8"/></svg>Odette F.</div>
    <div class="card-meta"><svg width="8" height="10"><path d="M4 10C1 6 0 4.5 0 3.5a4 4 0 018 0C8 4.5 7 6 4 10z" fill="#6aa3b8"/><circle cx="4" cy="3.6" r="1.4" fill="#f7f7f5"/></svg>San Diego, CA</div>
    <div class="card-meta"><b style="color:var(--meta)">$</b>10-15</div>
    <p class="card-bio">Lorem Ipsum is simply dummy text of the printing and typesetting indu stry. Lorem Ipsum has been the industry's standard dummy text ever since</p>
    <div class="view" style="margin:14px 0 0 32px">View Profile</div>
  </article>
</section>

<footer>
  <div class="abs footer"></div>
  <div class="abs stripe" style="top:968px"></div>
  <div class="abs fbox about">
    <h3>About KinWatch</h3>
    <p>Lorem Ipsum is simply dummy text of the printing and typesetting industry. Lorem Ipsum has been the industry's standard dummy text ever since the 1500s, when an unknown printer took a galley of type and scrambled it to make a type specimen book.</p>
    <a href="#">Read More...</a>
  </div>
  <div class="abs fbox contact">
    <div><span class="dot"></span>1-800-555-0142</div>
    <div><span class="dot"></span>info@KinWatch.com</div>
  </div>
  <div class="abs fbox news">
    <h3>Newsletter</h3>
    <ul><li>Parents: Post Your Job</li><li>Caregivers: Apply Jobs</li><li>Find the Right Match</li></ul>
  </div>
  <div class="abs fbox social">
    <h3>Get Social With Us</h3>
    <div class="icons"><span></span><span></span><span></span><span></span><span></span><span></span></div>
  </div>
  <h3 class="abs subscribe">Subscribe With Us!</h3>
  <div class="abs field">Your Email.........</div>
  <div class="abs send">Send</div>
  <div class="abs legal" style="left:188px">Home&nbsp; - &nbsp;About us - &nbsp;Privacy Policy &nbsp;- &nbsp;Terms &amp; Condition &nbsp;- &nbsp;Contact us</div>
  <div class="abs legal" style="left:720px">© 2014 Copyright &nbsp;All Rights Reserved KinWatch.com</div>
</footer>

</body>
</html>
```